Transformative School Model Needs a Website. I am easy to work with.

Greetings:
I am creating a K-12 school that is a complete and total re-imagination of what education can be for children, families, communities, and the planet. While we will begin as a K-12 school, I really see it as a complete life cycle education (birth to death). I'm looking for a website to describe my new transformational educational model. I anticipate having 7-8 pages. I have all the copy ready.
I am the Founder. I am easy to work with, an effective communicator, and I’m very good at knowing what I want and providing specific and concrete detail, examples, and direction to make sure I use your time wisely.

```html
<!DOCTYPE html>
<html lang="en">
<head>
<meta charset="utf-8">
<title>Luminous Unity School</title>
<link href="https://fonts.googleapis.com/css2?family=Cinzel:wght@400;500;600&family=Roboto:ital,wght@0,400;0,500;0,700;1,400&display=swap" rel="stylesheet">
<style>
:root{
  --navy:#17567f;
  --navy-deep:#0d4a72;
  --sky:#4fa6c9;
  --orange:#ff6a00;
  --amber:#ffb400;
  --text:#333333;
  --grey-band:#f0f0f0;
  --white:#ffffff;
}
*{margin:0;padding:0;box-sizing:border-box}
html,body{width:1200px;height:4280px;overflow:hidden}
body{position:relative;background:var(--white);font-family:"Roboto",Arial,sans-serif;color:var(--text)}
.abs{position:absolute}
.btn{position:absolute;display:flex;align-items:center;gap:8px;border-radius:24px;color:var(--white);font-weight:700;font-size:14px;background:linear-gradient(90deg,var(--amber),var(--orange))}
.btn .dot{width:26px;height:26px;border-radius:50%;border:1.5px solid rgba(255,255,255,.7)}
.heading{position:absolute;font-family:"Cinzel",Georgia,serif;font-weight:600;color:var(--navy);line-height:1.05;font-size:44px;letter-spacing:1px}
.body-copy{position:absolute;font-size:13px;line-height:1.5;color:var(--text)}

.site-header{position:absolute;left:0;top:0;width:1200px;height:100px;background:var(--white)}
.brand{position:absolute;left:130px;top:6px;width:162px;height:162px;border-radius:50%;background:var(--white);box-shadow:0 2px 6px rgba(0,0,0,.15);display:flex;align-items:center;justify-content:center;text-align:center;z-index:5}
.brand span{font-family:"Cinzel",Georgia,serif;font-weight:600;color:var(--navy);font-size:17px;line-height:1.2}
.call{position:absolute;left:720px;top:24px;display:flex;align-items:center;gap:10px;font-family:"Cinzel",Georgia,serif;color:var(--navy);font-size:18px}
.call .ic{width:22px;height:22px;border-radius:50%;background:var(--orange);display:flex;align-items:center;justify-content:center}
.nav{position:absolute;top:70px;left:365px;display:flex;font-size:14px;color:#222}
.nav span{margin-right:36px}

.hero-photo{position:absolute;left:0;top:100px;width:1200px;height:760px;background:linear-gradient(120deg,#7f9a4a 0%,#c9a441 35%,#9fb068 60%,#6f8f55 100%)}
.hero-title{position:absolute;left:560px;top:326px;width:620px;text-align:center;font-family:"Cinzel",Georgia,serif;font-weight:400;color:var(--white);font-size:40px;line-height:1.15;letter-spacing:1px;white-space:nowrap}

.card{position:absolute;width:433px;height:277px;background:#fafafa;border:1.5px solid var(--orange);border-radius:0 40px 0 40px;border-right-color:var(--amber);border-bottom-color:var(--amber);text-align:center}
.card .avatar{width:90px;height:90px;border-radius:50%;margin:24px auto 10px;background:linear-gradient(180deg,#e4d6c8,#6d4a2e)}
.card h4{color:var(--navy);font-size:18px;font-weight:700}
.card p{font-style:italic;font-size:12.5px;line-height:1.7;margin:14px 28px 0}

.footer-col h5{font-family:"Cinzel",Georgia,serif;font-weight:500;color:var(--white);font-size:20px;margin-bottom:18px}
.contact-row{display:flex;gap:12px;margin-bottom:16px;color:var(--white);font-size:13px;line-height:1.35}
.contact-row .ic{width:34px;height:34px;border-radius:50%;background:linear-gradient(135deg,var(--amber),var(--orange));flex:none;display:flex;align-items:center;justify-content:center}
.links{display:grid;grid-template-columns:140px 100px;row-gap:14px;color:var(--white);font-size:13px}
</style>
</head>
<body>

<header class="site-header">
  <div class="brand"><span>Luminous<br>Unity<br>School</span></div>
  <div class="call"><span class="ic"><svg width="12" height="12" viewBox="0 0 24 24"><path fill="#fff" d="M6.6 10.8a15 15 0 0 0 6.6 6.6l2.2-2.2c.3-.3.7-.4 1-.2 1.1.4 2.3.6 3.6.6.6 0 1 .4 1 1V20c0 .6-.4 1-1 1A17 17 0 0 1 3 4c0-.6.4-1 1-1h3.5c.6 0 1 .4 1 1 0 1.3.2 2.5.6 3.6.1.3 0 .7-.2 1z"/></svg></span>CALL US: 55 010 2024</div>
  <div class="btn" style="left:965px;top:18px;width:120px;height:38px;justify-content:center;font-family:Cinzel,serif;font-weight:500">&#9829; DONATE</div>
  <nav class="nav"><span>About</span><span>School Foundations</span><span>Curriculum</span><span>Pedagogy</span><span>Outcomes</span><span>Opening</span><span>Testimonials</span></nav>
</header>

<section class="hero">
  <div class="hero-photo" role="img" aria-label="Photo of smiling children hugging outdoors in a park"></div>
  <h1 class="hero-title">WELCOME TO LUMINOUS<br>UNITY SCHOOL</h1>
  <div class="btn" style="left:811px;top:450px;width:118px;height:38px;justify-content:center;font-family:Cinzel,serif;font-weight:500">&#9829; DONATE</div>
  <svg class="abs" style="left:0;top:680px" width="1200" height="200" viewBox="0 0 1200 200">
    <defs><linearGradient id="heroWave" x1="0" x2="1"><stop offset="0" stop-color="#ffb400"/><stop offset="1" stop-color="#ff5a00"/></linearGradient></defs>
    <path d="M0 110 C300 150 550 60 850 30 C1020 15 1130 70 1200 110 V200 H0Z" fill="url(#heroWave)"/>
    <path d="M0 100 C250 150 550 140 780 90 C950 60 1080 90 1200 180 V200 H0Z" fill="#fff"/>
  </svg>
</section>

<section class="philosophy">
  <svg class="abs" style="left:165px;top:915px" width="415" height="415" viewBox="0 0 415 415" role="img" aria-label="Decorative sacred geometry emblem">
    <defs><linearGradient id="ring" x1="0" y1="0" x2="1" y2="1"><stop offset="0" stop-color="#ffb400"/><stop offset="1" stop-color="#ff5a00"/></linearGradient></defs>
    <circle cx="207" cy="207" r="200" fill="#fff7ec" stroke="url(#ring)" stroke-width="7"/>
  </svg>
  <h2 class="heading" style="left:655px;top:922px">SPIRITUAL<br>PHILOSOPHY</h2>
  <p class="body-copy" style="left:657px;top:1030px;width:400px">Lorem ipsum dolor sit amet, consectetur adipiscing elit, sed do eiusmod tempor incididunt ut labore et dolore magna aliquuis ip sum suspendisse ultrices gravida. Risus commodo viverra mae cenas accumsan lacus vel facilisis. Sed ut perspiciatis unde om nis iste natus error sit voluptatem accusantium dolorem loque laudantium, totam rem aperiam, eaque ipsa quae ab illo inventore veritatis et quasi architecto beatae vitae dicta sunt explicabemo enim ipsam voluptatem quia voluptas sit aspernatur aut odit aut fugit, sed quia consequuntur magni dolores eo.</p>
  <div class="btn" style="left:657px;top:1237px;width:140px;height:46px;padding-left:8px"><span class="dot"></span>READ MORE</div>
</section>

<section class="about abs" style="left:0;top:1425px;width:1200px;height:585px;background:var(--grey-band)">
  <div class="abs" style="left:168px;top:87px;width:185px;height:218px;border:2px solid var(--sky);background:#c3dde8"></div>
  <div class="abs" role="img" aria-label="Photo of the founder standing in a library holding books" style="left:198px;top:114px;width:367px;height:367px;border-radius:0 40px 0 40px;background:linear-gradient(160deg,#8d7a62 0%,#d8c38f 55%,#b59a55 100%)"></div>
  <h2 class="heading" style="left:650px;top:118px">ABOUT ME</h2>
  <p class="body-copy" style="left:650px;top:195px;width:400px">Lorem ipsum dolor sit amet, consectetur adipiscing elit, sed do eiusmod tempor incididunt ut labore et dolore magna aliquuis ip sum suspendisse ultrices gravida. Risus commodo viverra mae cenas accumsan lacus vel facilisis. Sed ut perspiciatis unde om nis iste natus error sit voluptatem accusantium dolorem loque laudantium, totam rem aperiam, eaque ipsa quae ab illo inventore veritatis et quasi architecto beatae vitae dicta sunt explicabemo enim ipsam voluptatem quia voluptas sit aspernatur aut odit aut fugit, sed quia consequuntur magni dolores eo.</p>
  <div class="btn" style="left:650px;top:400px;width:140px;height:46px;padding-left:8px"><span class="dot"></span>READ MORE</div>
</section>

<section class="purpose">
  <h2 class="heading" style="left:150px;top:2165px">PURPOSE</h2>
  <p class="body-copy" style="left:150px;top:2235px;width:432px">Lorem ipsum dolor sit amet, consectetur adipiscing elit, sed do eiusm od tempor incididunt ut labore et dolore magna aliquuis ipsum suspe ndisse ultrices gravida. Risus commodo viverrLorem ipsum dolor am et, consectetur adipiscing elit, sed do eiusmod tempor incididunt ut labore et dolore magna aliquuis ipsum suspendisse ultrices gravida. Risus commodo viverra mae cenas accumsan lacus vel facilisis. Sed ut perspiciatis unde omnis iste natus error sit voluptatem accusantium dolorem loque laudantium, totam rem aperiam, eaque ipsa quae ab illo inventore veritatis et quasi architecto beatae vitae dicta sunt explica bemo enim ipsam voluptatem quia voluptas sit aspernatur aut odit fugit, sed quia consequuntur magni dolores eo.</p>
  <div class="btn" style="left:150px;top:2475px;width:140px;height:46px;padding-left:8px"><span class="dot"></span>READ MORE</div>
  <div class="abs" style="left:658px;top:2118px;width:180px;height:195px;border:1.5px solid var(--orange);border-top-color:var(--amber);background:#fff6ee"></div>
  <div class="abs" role="img" aria-label="Photo of a happy family with two children outdoors" style="left:685px;top:2143px;width:367px;height:367px;border-radius:0 40px 0 40px;background:linear-gradient(160deg,#5f8a3c,#9bb86a 45%,#6d9fc4)"></div>
</section>

<section class="statement abs" style="left:0;top:2655px;width:1200px;height:515px;background:linear-gradient(110deg,#ffbe10 0%,#ffa200 40%,#ff7300 75%,#ff5a00 100%)">
  <h2 class="abs" style="left:0;top:120px;width:1200px;text-align:center;font-family:Cinzel,serif;font-weight:400;color:#fff;font-size:44px;line-height:1.05">STATEMENT OF<br>ONENESS WITH EQUIT</h2>
  <p class="abs" style="left:270px;top:250px;width:660px;text-align:center;font-style:italic;font-weight:400;color:#fff;font-size:21px;line-height:1.3">“ Lorem ipsum dolor sit amet, consectetur dipis cing elit, sed do eiusmod tempor incididunt ut labore et dolore magna aliqua. Quis ipsum suspe ndisse ultrices gravida. Risus commodo viverra maecenas accumsan lacus vel facilisis.”</p>
</section>

<section class="testimonials">
  <h2 class="heading" style="left:0;top:3290px;width:1200px;text-align:center;font-size:38px">TESTIMONIALS</h2>
  <svg class="abs" style="left:98px;top:3488px" width="20" height="30" viewBox="0 0 20 30"><path d="M16 3 4 15l12 12" fill="none" stroke="var(--navy)" stroke-width="4"/></svg>
  <svg class="abs" style="left:1086px;top:3488px" width="20" height="30" viewBox="0 0 20 30"><path d="M4 3l12 12L4 27" fill="none" stroke="var(--navy)" stroke-width="4"/></svg>
  <div class="card" style="left:150px;top:3390px"><div class="avatar" role="img" aria-label="Portrait photo of a reviewer at sunset"></div><h4>Quiet River</h4><p>“ Lorem ipsum dolor sit amet, consectetur adipiscing elit, sed do eiusmod tempor incididunt ut labore et dolore magna aliqua. Quis ipsum suspendisse ultrices gravida. Risus commodo viverra maecenas accumsan lacus vel facilisis. ”</p></div>
  <div class="card" style="left:617px;top:3390px"><div class="avatar" role="img" aria-label="Portrait photo of a reviewer at sunset"></div><h4>Quiet River</h4><p>“ Lorem ipsum dolor sit amet, consectetur adipiscing elit, sed do eiusmod tempor incididunt ut labore et dolore magna aliqua. Quis ipsum suspendisse ultrices gravida. Risus commodo viverra maecenas accumsan lacus vel facilisis. ”</p></div>
</section>

<footer class="site-footer">
  <svg class="abs" style="left:0;top:3780px" width="1200" height="500" viewBox="0 0 1200 500">
    <defs>
      <linearGradient id="footOrange" x1="0" x2="1"><stop offset="0" stop-color="#ffb400"/><stop offset="1" stop-color="#ff6a00"/></linearGradient>
      <linearGradient id="footBlue" x1="0" x2="1"><stop offset="0" stop-color="#56a9cc"/><stop offset="1" stop-color="#0c4e78"/></linearGradient>
    </defs>
    <path d="M0 40 C250 110 450 0 700 10 C900 18 1080 50 1200 90 V500 H0Z" fill="url(#footOrange)"/>
    <path d="M0 120 C200 160 400 150 650 80 C850 25 1050 30 1200 100 V500 H0Z" fill="url(#footBlue)"/>
  </svg>
  <div class="abs" style="left:150px;top:3985px;width:195px;height:195px;display:flex;align-items:center;gap:10px;flex-direction:column;justify-content:center">
    <div style="width:18px;height:18px;border-radius:50%;background:#fff"></div>
    <span style="font-family:Cinzel,serif;font-weight:600;color:#fff;font-size:20px;text-align:center;line-height:1.2">Luminous<br>Unity School</span>
  </div>
  <div class="abs footer-col" style="left:473px;top:3978px">
    <h5>CONTACT</h5>
    <div class="contact-row"><span class="ic"><svg width="14" height="16" viewBox="0 0 24 24"><path fill="#fff" d="M12 2a7 7 0 0 0-7 7c0 5 7 13 7 13s7-8 7-13a7 7 0 0 0-7-7zm0 9.5A2.5 2.5 0 1 1 12 6.5a2.5 2.5 0 0 1 0 5z"/></svg></span><span>Address: 12 Lantern Way<br>Meadow Vale</span></div>
    <div class="contact-row"><span class="ic"><svg width="14" height="14" viewBox="0 0 24 24"><path fill="#fff" d="M6.6 10.8a15 15 0 0 0 6.6 6.6l2.2-2.2c.3-.3.7-.4 1-.2 1.1.4 2.3.6 3.6.6.6 0 1 .4 1 1V20c0 .6-.4 1-1 1A17 17 0 0 1 3 4c0-.6.4-1 1-1h3.5c.6 0 1 .4 1 1 0 1.3.2 2.5.6 3.6.1.3 0 .7-.2 1z"/></svg></span><span>Phone:<br>(01) 555 0147</span></div>
    <div class="contact-row"><span class="ic"><svg width="14" height="12" viewBox="0 0 24 20"><path fill="#fff" d="M2 2h20v16H2zm10 8 9-6H3z"/></svg></span><span>Email:<br>hello@luminousunity.org</span></div>
  </div>
  <div class="abs footer-col" style="left:825px;top:3978px">
    <h5>LINKS</h5>
    <div class="links"><span>About</span><span>Outcomes</span><span>School Foundations</span><span>Opening</span><span>Curriculum</span><span>Testimonials</span><span>Pedagogy</span><span>Donate</span></div>
  </div>
  <p class="abs" style="left:0;top:4232px;width:1200px;text-align:center;color:#fff;font-size:12px">Copyright © 2023 Luminous Unity School. All rights reserved.</p>
</footer>

</body>
</html>
```